StoneHarbor - Business Card and Letterhead

After having received some fantastic submissions in our recent logo design project, I would now like to extend our branding to letterheads and business cards.
StoneHarbor is a consulting service in the Construction Industry. We deal with both residential and commercial projects, and our clients include Architects, Builders, Tradespeople and Home Owners.
The designs should be simple and effective, convey personal service and professionalism, and display some level of creativity.
For both the business cards and letterhead, a white card stock will be used. This project is for business cards and letterheads only. Our new logo is attached for use.
The designs should incorporate our two main colours which are Blue (RGB 14,92,143) and Green (RGB 132,194,37).
For the time being, please submit all designs showing generic information including name, mobile number, email, postal address and website details. No fax number or physical address is required. I will provide our actual contact details once a final design has been selected.
I encourage you to interpret this brief in your own creative way, and look forward to some quality submissions.
Thanks!
Lee
StoneHarbor.

```html
<!DOCTYPE html>
<html lang="en">
<head>
<meta charset="utf-8">
<title>StoneHarbor – Business Card</title>
<link rel="stylesheet" href="https://fonts.googleapis.com/css2?family=Cabin:wght@400;600;700&display=swap">
<style>
  :root {
    --blue: rgb(14, 92, 143);
    --blue-band: #1f6fa3;
    --green: rgb(132, 194, 37);
    --green-dark: #3f8a12;
    --ink: #2b2b2b;
    --muted: #555555;
    --paper: #ffffff;
    --backdrop: #e9ecef;
  }
  * { box-sizing: border-box; margin: 0; padding: 0; }
  html, body { width: 1200px; height: 900px; overflow: hidden; }
  body {
    background: var(--backdrop);
    font-family: "Cabin", "Gill Sans", sans-serif;
    position: relative;
  }
  .card {
    position: absolute;
    left: 50%;
    transform: translateX(-50%);
    box-shadow: 0 10px 28px rgba(0, 0, 0, 0.18);
    overflow: hidden;
  }

  /* Back of card */
  .card-back {
    top: 50px;
    width: 525px;
    height: 300px;
    background: radial-gradient(ellipse at 45% 40%, #8fd12e 0%, var(--green) 35%, var(--green-dark) 100%);
    display: flex;
    align-items: center;
    justify-content: center;
  }
  .card-back .brand {
    display: flex;
    align-items: center;
    gap: 10px;
    font-size: 34px;
    font-weight: 600;
    color: var(--paper);
    letter-spacing: 0.2px;
  }
  .card-back .brand-square {
    width: 24px;
    height: 24px;
    background: var(--paper);
  }

  /* Front of card */
  .card-front {
    top: 400px;
    width: 700px;
    height: 400px;
    background: var(--paper);
  }
  .card-front .brand {
    position: absolute;
    left: 40px;
    top: 30px;
    display: flex;
    align-items: center;
    gap: 12px;
    font-size: 52px;
    font-weight: 700;
    color: var(--blue);
    line-height: 1;
  }
  .card-front .brand-square {
    width: 36px;
    height: 36px;
    background: var(--green);
  }
  .contact {
    position: absolute;
    left: 62px;
    top: 108px;
    color: var(--ink);
    font-size: 16px;
    line-height: 1.28;
  }
  .contact .person-name {
    font-size: 22px;
    color: var(--blue);
    letter-spacing: 0.5px;
  }
  .contact .person-role {
    color: var(--muted);
    font-size: 16px;
    margin-bottom: 4px;
  }
  .contact .label {
    color: var(--blue);
    display: inline-block;
    width: 58px;
  }
  .contact .address { margin-top: 4px; }
  .contact .website { color: var(--blue); }
  .card-front .swoosh {
    position: absolute;
    left: 0;
    bottom: 0;
    width: 700px;
    height: 170px;
  }
</style>
</head>
<body>
  <section class="card card-back" aria-label="Business card, back">
    <div class="brand"><span class="brand-square"></span>StoneHarbor</div>
  </section>

  <section class="card card-front" aria-label="Business card, front">
    <div class="brand"><span class="brand-square"></span>StoneHarbor</div>

    <div class="contact">
      <p class="person-name">DANIEL CORWIN</p>
      <p class="person-role">managing director</p>
      <p><span class="label">phone</span>212 640 31 97</p>
      <p><span class="label">mobile</span>917 382 46 05</p>
      <p><span class="label">email</span>info@stoneharbor.com</p>
      <p class="address">48 Quarry Lane, Millbrook, New York 12545</p>
      <p class="website">www.stoneharbor.com</p>
    </div>

    <svg class="swoosh" viewBox="0 0 700 170" aria-hidden="true">
      <path d="M0 40 C 180 80, 420 150, 700 120 L700 170 L0 170 Z" fill="var(--blue-band)"/>
      <path d="M0 40 C 180 80, 420 150, 700 120 L700 112 C 430 138, 200 70, 0 28 Z" fill="var(--paper)"/>
      <path d="M220 66 C 380 120, 540 125, 700 108 L700 100 C 540 116, 390 110, 220 66 Z" fill="var(--green)"/>
    </svg>
  </section>
</body>
</html>
```